Ardenwell Building and Property Services needs a business card design

We need a business card design for our building and property services business. We already have a logo we just need a creative design and layout on a business card. Emphasis on clean, modern, professional.
Our client targets are mainly body corporates, building managers, construction managers.
We are a building services company that lean more to structural repair of buildings, through concrete rectification and carbon fibre strengthening.
We also refurbish facades, rendering, painting etc
We target higher end body corporates in prestigious locations, hence why we'd like our cards to reflect professionalism, strength, efficiency

Target Market(s)

body corporates, building managers, construction managers

Industry/Entity Type

Construction

Contact Information for Business Card

Ardenwell is the main word, with 'Building and Property Services' underneath.
Level 17, 82 Harlow Street
MERRIDALE
Melbourne
Vic 3094
T: 9518 2736
Duncan Ferris - Director
dunardenwell@mailbox-example.com

Requirements
Must have
• Stand out on the back of the card- strong/ bold, company logo
• All of the contact details written above
Should not have
• I'd like the card to stand out, especially on the back. Id like the company logo to be prominent, although feel free to be creative around it. But remain clean and professional

```html
<!DOCTYPE html>
<html lang="en">
<head>
<meta charset="utf-8">
<title>Ardenwell Building and Property Services – Business Card</title>
<link href="https://fonts.googleapis.com/css2?family=Cinzel:wght@400;600&family=Lato:wght@400;700&display=swap" rel="stylesheet">
<style>
  :root{
    --bg:#e9eaec;
    --card:#ffffff;
    --band-top:#c4c4c4;
    --band-bottom:#a9a9a9;
    --blue:#2f8fd8;
    --blue-dark:#1f6fb4;
    --ink:#5a5a5a;
    --ink-soft:#7a7a7a;
    --shadow:rgba(0,0,0,.18);
  }
  *{box-sizing:border-box;margin:0;padding:0}
  html,body{width:1200px;height:900px;overflow:hidden}
  body{background:var(--bg);font-family:'Lato',sans-serif;position:relative}

  .card{
    position:absolute;top:290px;width:540px;height:310px;
    background:var(--card);
    box-shadow:0 10px 30px var(--shadow);
    overflow:hidden;
  }
  .card--front{left:45px}
  .card--back{left:615px}

  .band{
    position:absolute;left:0;right:0;
    background:linear-gradient(180deg,var(--band-top),var(--band-bottom));
  }
  .band::before,.band::after{
    content:"";position:absolute;left:0;right:0;height:2px;background:var(--blue);
  }
  .band::before{top:-6px}
  .band::after{bottom:-6px}

  /* front */
  .card--front .band{top:88px;height:50px}
  .band__marker{
    position:absolute;left:0;top:15px;width:0;height:0;
    border-top:10px solid transparent;border-bottom:10px solid transparent;
    border-left:10px solid var(--blue);
  }
  .holder{
    position:absolute;left:36px;top:0;height:50px;display:flex;align-items:center;gap:8px;
    color:#fff;
  }
  .holder__name{font-size:22px;font-weight:400}
  .holder__divider{width:1.5px;height:22px;background:#fff}
  .holder__role{font-size:13px;letter-spacing:.5px;text-transform:uppercase}

  .front-mark{
    position:absolute;right:34px;top:32px;display:flex;align-items:center;gap:10px;
  }
  .front-mark__square{width:14px;height:14px;background:var(--blue)}
  .front-mark__name{font-family:'Cinzel',serif;font-weight:600;font-size:24px;color:var(--blue);letter-spacing:2px}

  .contacts{position:absolute;left:34px;top:162px;list-style:none;color:var(--ink);font-size:14.5px}
  .contacts li{display:flex;align-items:center;gap:9px;line-height:19px}
  .contacts .icon{width:15px;height:15px;flex:none}
  .contacts .address{align-items:flex-start;margin-top:14px}
  .contacts .address .icon{margin-top:2px}

  .front-tagline{
    position:absolute;right:34px;bottom:36px;text-align:right;
    font-family:'Cinzel',serif;color:var(--ink);font-size:17px;line-height:22px;letter-spacing:.5px;
  }

  /* back */
  .back-mark{
    position:absolute;left:0;right:0;top:92px;display:flex;flex-direction:column;align-items:center;
  }
  .back-mark__row{display:flex;align-items:center;gap:14px}
  .back-mark__square{width:22px;height:22px;background:var(--blue)}
  .back-mark__name{font-family:'Cinzel',serif;font-weight:600;font-size:46px;color:var(--blue);letter-spacing:4px}
  .back-mark__tagline{
    margin-top:4px;font-family:'Cinzel',serif;font-size:11.5px;letter-spacing:2px;color:var(--ink-soft);text-transform:uppercase;
  }
  .card--back .band{bottom:0;height:48px}
  .card--back .band::after{display:none}
</style>
</head>
<body>

<section class="card card--front" aria-label="Business card front">
  <div class="front-mark">
    <span class="front-mark__square"></span>
    <span class="front-mark__name">ARDENWELL</span>
  </div>

  <div class="band">
    <span class="band__marker"></span>
    <div class="holder">
      <span class="holder__name">Duncan Ferris</span>
      <span class="holder__divider"></span>
      <span class="holder__role">Director</span>
    </div>
  </div>

  <ul class="contacts">
    <li>
      <svg class="icon" viewBox="0 0 16 16" aria-hidden="true"><circle cx="8" cy="8" r="8" fill="#2f8fd8"/><path d="M5 4.5l1.6-.4.9 2-1 .8c.5 1 1.2 1.7 2.2 2.2l.8-1 2 .9-.4 1.6c-3.3.2-6.3-2.8-6.1-6.1z" fill="#fff"/></svg>
      <span>9518 2736</span>
    </li>
    <li>
      <svg class="icon" viewBox="0 0 16 16" aria-hidden="true"><circle cx="8" cy="8" r="8" fill="#2f8fd8"/><rect x="5.5" y="3.8" width="5" height="3" fill="#fff"/><rect x="4" y="6.5" width="8" height="4" rx="1" fill="#fff"/><rect x="5.5" y="9.5" width="5" height="2.8" fill="#fff" stroke="#2f8fd8" stroke-width=".6"/></svg>
      <span>9518 2736</span>
    </li>
    <li>
      <svg class="icon" viewBox="0 0 16 16" aria-hidden="true"><circle cx="8" cy="8" r="8" fill="#2f8fd8"/><rect x="4" y="5" width="8" height="6" fill="#fff"/><path d="M4 5l4 3.2L12 5" fill="none" stroke="#2f8fd8" stroke-width="1"/></svg>
      <span>dunardenwell@mailbox-example.com</span>
    </li>
    <li class="address">
      <svg class="icon" viewBox="0 0 16 16" aria-hidden="true"><circle cx="8" cy="8" r="8" fill="#2f8fd8"/><path d="M8 3.5a3 3 0 0 0-3 3c0 2.3 3 5.8 3 5.8s3-3.5 3-5.8a3 3 0 0 0-3-3z" fill="#fff"/><circle cx="8" cy="6.5" r="1.1" fill="#2f8fd8"/></svg>
      <span>Level 17, 82 Harlow Street<br>MERRIDALE<br>Melbourne, Vic 3094</span>
    </li>
  </ul>

  <p class="front-tagline">Building<br>and Property Services</p>
</section>

<section class="card card--back" aria-label="Business card back">
  <div class="back-mark">
    <div class="back-mark__row">
      <span class="back-mark__square"></span>
      <span class="back-mark__name">ARDENWELL</span>
    </div>
    <p class="back-mark__tagline">Building and Property Services</p>
  </div>
  <div class="band"></div>
</section>

</body>
</html>
```